Women Web Portal

We are developing an internet portal with content created by and for women in Latin America.
This portal will contain different categories focused on relevant topics for women who are at the same time mothers, lovers, workers, pet-owners, ...

We are looking for design that are at the same time uncluttered, easy-to-use and obvious, and comfy. Pastel colours, buttons using traditional fonts, large space for pictures, highlighted social elements,...

Our target being the middle-class women, we want a design that feels comfortable, real, a bit trendy and traditional, not a Tarsk & Welmore design, something women can relate to and feel comfortable enough to come back and participate.

Examples of websites:
www.dishtable.example
mujer.qelvo.example
www.cabellorinva.example
www.fourneau.example
Updates

Hi dear designers. After viewing some first drafts, I have updated the brief so you might have a better understanding of what we are looking for.

Thanks

Reason: We've been away for a while, unavailable to provide adequate feedback to the designs already sent. So we're extending the deadline in order to give time to everyone to adapt their work according to the feedback we'll be providing today.

Target Market(s)

Women between 25 and 50 years from Latin America. Mainly mothers: basically, we want women to interact with each other and with the content of the site so they create a strong community.

Advertisingly speaking, we want to have users, contents and FMCG brands to live together on this website.

Industry/Entity Type

Internet

Requirements
Must have
• Pastel colours for category tabs. Comfortable look & feel.

The design should include 3 different pages:
- Homepage
- Article page
- User profile

The page will be done in responsive design, so design should be thought to be adapted according to the browser (2 or 3 columns).

Thanks for doing it as a PSD file .

The design should also include:
- 8 category tabs
- Space for 728x90px and 300x600px advertising format.
- A relevant menu bar at the beginning of each page
Nice to have
• News feed/best content/most active comments zone: we need to bring forward content to our users so they'll be attracted to visit more pages of the website.

Small format to register (account).

Slider or any other moving objects.

Any idea that would facilitate and increase user participation
Should not have
• Actual text. please use Lorem Ipsum.

```html
<!DOCTYPE html>
<html lang="en">
<head>
<meta charset="utf-8">
<title>Velaria – Sapiente Delectus</title>
<link href="https://fonts.googleapis.com/css2?family=Noto+Sans:ital,wght@0,400;0,700;1,400&family=Noto+Serif:ital,wght@1,700&family=Fondamento&family=Oleo+Script&display=swap" rel="stylesheet">
<style>
  :root {
    --purple: #5c0499;
    --yellow: #ffd21f;
    --white: #ffffff;
    --headline: #6565f5;
    --subline: #2bd42b;
    --body: #7a7a7a;
    --rule: #cfcfcf;
    --nav-text: #7a7a7a;
    --bullet: #8a22c9;
    --bullet-active: #7ee02b;
    --banner-light: #8fbcd6;
    --banner-deep: #3f86b4;
    --photo-bg: #e6e4e1;
    --photo-tone: #d9c4ac;
    --title-purple: #8b2aa8;
    --travel-gold: #e9ad2a;
  }
  * { box-sizing: border-box; margin: 0; padding: 0; }
  html, body { width: 1084px; height: 1200px; overflow: hidden; background: var(--white); }
  body { font-family: Verdana, "Noto Sans", sans-serif; position: relative; }

  .top-bar {
    position: absolute; left: 28px; top: 0; width: 1027px; height: 55px;
    background: var(--purple); display: flex; align-items: center;
  }
  .brand {
    display: flex; align-items: center; gap: 12px; margin-left: 8px;
    color: var(--white); font-size: 30px; font-weight: 400; letter-spacing: 0.5px;
  }
  .brand-mark { width: 40px; height: 40px; border-radius: 50%; background: var(--white); opacity: .9; }
  .account-link {
    margin-left: auto; color: var(--yellow); font-weight: 700; font-size: 20px;
    letter-spacing: .5px; margin-right: 22px;
  }
  .social { display: flex; gap: 24px; align-items: center; margin-right: 38px; }
  .social svg { display: block; }

  .banner {
    position: absolute; left: 28px; top: 62px; width: 1027px; height: 127px;
    background: linear-gradient(180deg, var(--banner-light) 0%, var(--banner-deep) 100%);
  }
  .banner-title {
    position: absolute; right: 62px; top: 16px; color: var(--travel-gold);
    font-family: "Fondamento", serif; font-size: 46px;
  }

  .category-nav {
    position: absolute; left: 28px; top: 208px; width: 1027px;
    display: flex; justify-content: space-between;
  }
  .category-tab {
    width: 124px; text-align: center; color: var(--nav-text); font-size: 17px;
    padding-bottom: 6px; border-bottom: 3px solid var(--rule);
  }
  .category-tab .dot {
    display: block; width: 17px; height: 17px; border-radius: 50%; margin: 2px auto 0;
    background: radial-gradient(circle at 35% 35%, #d9a4ff, var(--bullet) 60%, #4c0679);
  }
  .category-tab.is-active .dot {
    background: radial-gradient(circle at 35% 35%, #e6ffc4, var(--bullet-active) 60%, #3f9d0e);
  }

  .article { position: absolute; left: 28px; top: 290px; width: 577px; }
  .article-title {
    text-align: center; color: var(--headline); font-size: 57px; font-weight: 700; line-height: 1.1;
  }
  .article-lead {
    margin: 14px 22px 0; text-align: center; color: var(--subline);
    font-family: "Noto Serif", serif; font-style: italic; font-weight: 700; font-size: 17px; line-height: 1.35;
  }
  .article-body { margin-top: 30px; }
  .article-body p {
    color: var(--body); font-size: 17.2px; letter-spacing: .15px; line-height: 19.7px;
    text-align: justify; margin-bottom: 19.7px;
  }
  .article-body strong { font-weight: 700; }

  .ad-tower {
    position: absolute; left: 632px; top: 296px; width: 423px; height: 846px;
    background: linear-gradient(160deg, var(--photo-bg) 0%, #d8cfc4 45%, var(--photo-tone) 70%, #e8e6e3 100%);
  }
  .ad-tower-title {
    position: absolute; left: 32px; top: 680px; color: var(--title-purple);
    font-family: "Oleo Script", serif; font-weight: 400; font-size: 48px;
    transform: scaleX(.72); transform-origin: left;
  }
</style>
</head>
<body>
  <header class="top-bar">
    <div class="brand"><span class="brand-mark"></span><span class="brand-name">Velaria</span></div>
    <span class="account-link">login/register</span>
    <div class="social">
      <svg width="50" height="34" viewBox="0 0 50 34" aria-label="mail">
        <rect x="2" y="2" width="46" height="30" fill="var(--yellow)" stroke="var(--purple)" stroke-width="2"/>
        <path d="M3 3 L25 20 L47 3 M3 31 L20 16 M47 31 L30 16" fill="none" stroke="var(--purple)" stroke-width="2"/>
      </svg>
      <svg width="50" height="44" viewBox="0 0 50 44" aria-label="chat">
        <ellipse cx="18" cy="16" rx="16" ry="12" fill="var(--yellow)"/>
        <path d="M8 25 L4 34 L16 27 Z" fill="var(--yellow)"/>
        <ellipse cx="34" cy="26" rx="14" ry="10" fill="var(--yellow)" stroke="var(--purple)" stroke-width="2"/>
        <path d="M42 34 L47 42 L36 35 Z" fill="var(--yellow)"/>
      </svg>
      <svg width="44" height="44" viewBox="0 0 44 44" aria-label="social link"><rect x="1" y="1" width="42" height="42" rx="8" fill="var(--yellow)"/></svg>
      <svg width="44" height="44" viewBox="0 0 44 44" aria-label="social link"><rect x="1" y="1" width="42" height="42" rx="8" fill="var(--yellow)"/></svg>
      <svg width="50" height="42" viewBox="0 0 50 42" aria-label="search">
        <circle cx="16" cy="15" r="11" fill="none" stroke="var(--yellow)" stroke-width="6"/>
        <path d="M25 22 L46 38" stroke="var(--yellow)" stroke-width="9" stroke-linecap="round"/>
      </svg>
    </div>
  </header>

  <div class="banner" role="img" aria-label="Travel banner photograph: coastal bay with hills and sea">
    <span class="banner-title">wise Travel</span>
  </div>

  <nav class="category-nav">
    <div class="category-tab is-active">home<span class="dot"></span></div>
    <div class="category-tab">article<span class="dot"></span></div>
    <div class="category-tab">lorem<span class="dot"></span></div>
    <div class="category-tab">dolor<span class="dot"></span></div>
    <div class="category-tab">consectetur<span class="dot"></span></div>
    <div class="category-tab">occaecat<span class="dot"></span></div>
    <div class="category-tab">cupidatat<span class="dot"></span></div>
    <div class="category-tab">culpa<span class="dot"></span></div>
  </nav>

  <main class="article">
    <h1 class="article-title">Sapiente Delectus</h1>
    <p class="article-lead">Neque porro quisquam est qui dolorem ipsum quia dolor sit amet, consectetur, adipisci velit...</p>
    <div class="article-body">
      <p>Lorem ipsum dolor sit amet, consectetur adipisicing elit, sed do eiusmod tempor incididunt ut labore et dolore magna aliqua. Ut enim ad <strong>minim veniam</strong>, quis nostrud exercitation ullamco laboris nisi ut aliquip ex ea commodo consequat. Duis aute irure dolor in reprehenderit in voluptate velit esse cillum dolore eu fugiat nulla pariatur. Excepteur sint occaecat cupidatat non proident, sunt in culpa qui officia deserunt mollit anim id est laborum.</p>
      <p>At vero eos et accusamus et iusto odio dignissimos ducimus qui blanditiis praesentium voluptatum deleniti atque corrupti quos dolores et quas molestias excepturi sint occaecati cupiditate non provident, similique sunt in culpa qui officia deserunt mollitia animi, id est laborum et dolorum fuga. Et harum quidem <strong>rerum facilis</strong> est et expedita distinctio. Nam libero tempore, cum soluta nobis est eligendi optio cumque nihil impedit quo minus id quod maxime placeat facere possimus, omnis voluptas assumenda est, omnis dolor repellendus. Temporibus autem quibusdam et aut officiis debitis aut rerum necessitatibus saepe eveniet ut et voluptates repudiandae sint et molestiae non recusandae. Itaque earum rerum hic <strong>tenetur a sapiente delectus</strong>, ut aut reiciendis voluptatibus maiores alias consequatur aut perferendis doloribus asperiores repellat.</p>
      <p>Temporibus autem quibusdam et aut officiis debitis aut rerum necessitatibus saepe eveniet ut et voluptates repudiandae sint et molestiae non recusandae consequatur aut perferendis doloribus asperiores repellat.</p>
      <p>Duis aute irure dolor in reprehenderit in voluptate velit esse cillum dolore eu fugiat nulla pariatur. Excepteur sint occaecat cupidatat non proident, sunt in culpa qui officia deserunt mollit anim id est laborum.</p>
    </div>
  </main>

  <aside class="ad-tower" role="img" aria-label="Fashion advertisement photograph: model in a light jacket and jeans">
    <span class="ad-tower-title">Fashion house</span>
  </aside>
</body>
</html>
```